Computer consultant website

Vexlo Software is a newly started computer consulting company. It's a small one-man company that provides mostly Android applications but also websites in collaboration with designers. I'm running this company on the side of full time university studies.

I'm in need of a website which will function as:
Primarily - I'll direct potential clients to the page so they can read about the company, what i offer and past work.
Secondarily - Making my company visible through the web and maybe getting new clients.

The final design should look modern, clean and professional.

Pages that will be in the final website are (Note that it's not the exact titles as the page will not be in english):
* About
* Services (what Vexlo offers)
* Portfolio/work
* Short news (like PlanHives "News and press")
* Contact.

Inspiration
http://www.planhive.example/design/87836
http://www.brambleorb.example/
http://www.planhive.example/design/845881
http://www.planhive.example/design/1369424 - Lighter design, however a bit cluttered.

No programming code is needed delivered at all. Focus on designing rather then coding.

If you have any questions, do not hesitate to send me a message.

Target Market(s)

Non-technical entrepreneurs and small companies.

Industry/Entity Type

University

Requirements
Must have
• Must have my company logo (see attachment).

Must in any way use both colors from my logo.

A way to logically rearrange content to fit smaller screens. I will implement this design so that it can be pleasantly viewed on mobile devices. You don't necessarily need to provide exactly how the design would look on mobile devices.

I need the following types of page designs:
* Landing page
* Content page
* Portfolio/work (with accompanying inside/clicked) page

Landing/start page must in any way include at least the information:
* Shorter version of "About Vexlo"
* At least 1 most recent portfolio/work entry
* At least 1 most recent news entry
* Services that Vexlo offers.
Nice to have
Should not have
• Testimonials or newsletter.

```html
<!DOCTYPE html>
<html lang="en">
<head>
<meta charset="utf-8">
<title>Vexlo Software</title>
<link rel="stylesheet" href="https://fonts.googleapis.com/css2?family=Fira+Sans+Extra+Condensed:wght@300&family=Open+Sans:wght@400;600&family=PT+Sans+Narrow:wght@400;700&display=swap">
<style>
:root{
  --blue:#2f80e6;
  --blue-text:#3a86e8;
  --ink:#2f2f2f;
  --body:#666;
  --topbar:#262626;
  --footer:#292929;
  --panel:#1f2327;
  --card:#f1f1f1;
  --rule:#d6d6d6;
}
*{margin:0;padding:0;box-sizing:border-box}
html,body{width:1057px;height:1200px;overflow:hidden;background:#fff}
body{position:relative;font-family:"PT Sans Narrow",sans-serif;color:var(--body)}
a{text-decoration:none;color:inherit}
.abs{position:absolute}

/* top bar */
.topbar{left:0;top:0;width:1057px;height:61px;background:var(--topbar)}
.main-nav a{position:absolute;top:22px;font-family:"Open Sans",sans-serif;font-size:10.5px;letter-spacing:.5px;color:#e8e8e8}
.main-nav a.active{color:var(--blue-text)}
.social span{position:absolute;top:17px;width:26px;height:26px;border-radius:50%;background:var(--blue);border:1px solid #1d5fae}

/* header */
.brand{left:147px;top:74px;display:flex;align-items:center;gap:14px}
.brand-dot{width:56px;height:56px;border-radius:50%;background:var(--blue)}
.brand-name{font-family:"PT Sans Narrow",sans-serif;font-weight:700;font-size:58px;color:#333;line-height:1}
.search{left:653px;top:97px;width:256px;height:29px;border:1px solid #d4d4d4;display:flex}
.search span{flex:1;font-family:"Open Sans",sans-serif;font-style:italic;font-size:10.5px;color:#888;letter-spacing:.6px;padding:7px 0 0 11px}
.search b{width:39px;background:var(--blue);color:#fff;font-family:"Open Sans",sans-serif;font-weight:600;font-size:11px;letter-spacing:1px;text-align:center;line-height:27px}

/* hero */
.hero-photo{left:0;top:164px;width:1057px;height:324px;background:linear-gradient(90deg,#e4e2e2 0%,#d8d0cc 30%,#cfc5c2 50%,#d9c8cf 70%,#e5e3e6 100%)}
.hero-panel{left:149px;top:164px;width:286px;height:324px;background:var(--panel);text-align:center}
.hero-title{position:absolute;left:0;top:16px;width:286px;font-family:"Fira Sans Extra Condensed",sans-serif;font-weight:300;font-size:37px;line-height:46px;color:var(--blue-text)}
.hero-rule{position:absolute;left:34px;width:215px;height:1px;background:#3d4248}
.hero-text{position:absolute;left:37px;top:132px;width:212px;font-size:12.4px;line-height:22.7px;letter-spacing:.1px;color:#ddd}
.hero-btn{position:absolute;left:79px;top:258px;width:129px;height:33px;background:#ececec;font-family:"Fira Sans Extra Condensed",sans-serif;font-weight:300;font-size:17px;line-height:33px;color:var(--blue-text)}

/* intro */
.h2{font-family:"PT Sans Narrow",sans-serif;font-weight:700;font-size:15px;letter-spacing:.6px;color:var(--ink)}
.h2 em{font-style:normal;color:var(--blue-text)}
.copy{font-size:11.6px;line-height:24.3px;letter-spacing:.35px;color:var(--body)}
.more-link{font-family:"Open Sans",sans-serif;font-weight:600;font-size:8.6px;letter-spacing:.8px;color:var(--blue-text);display:flex;align-items:center;gap:5px}
.more-link.dark{color:var(--ink)}
.arrow{width:0;height:0;border-top:3.5px solid transparent;border-bottom:3.5px solid transparent;border-left:4.5px solid currentColor}
.list li{list-style:none;position:absolute;left:18px;font-size:11.6px;letter-spacing:.35px;color:var(--blue-text);white-space:nowrap}
.list li::before{content:"";position:absolute;left:-18px;top:5px;border-top:3.5px solid transparent;border-bottom:3.5px solid transparent;border-left:4.5px solid var(--ink)}
.divider{left:147px;top:748px;width:763px;border-top:1px dotted #bdbdbd}

/* cards */
.card{top:783px;width:246px;height:310px;background:var(--card)}
.card-img{position:absolute;left:0;top:0;width:246px;height:154px}
.card-notch{position:absolute;left:15px;top:154px;border-left:7px solid transparent;border-right:7px solid transparent;border-top:7px solid #8ea0b0}
.card h3{position:absolute;left:16px;top:166px;font-family:"PT Sans Narrow",sans-serif;font-weight:700;font-size:15.5px;letter-spacing:.8px;color:var(--ink)}
.card h4{position:absolute;left:16px;top:190px;font-family:"Open Sans",sans-serif;font-weight:400;font-size:8px;letter-spacing:.8px;color:#555}
.card hr{position:absolute;left:16px;top:209px;width:213px;border:0;border-top:1px solid var(--rule)}
.card p{position:absolute;left:16px;top:214px;width:216px;font-size:10.2px;line-height:21px;letter-spacing:.3px;color:var(--body)}
.card .more-link{position:absolute;left:16px;top:290px}

/* footer */
.footer{left:0;top:1145px;width:1057px;height:55px;background:var(--footer)}
.copyright{position:absolute;left:151px;top:21px;font-size:9.8px;color:#888}
.copyright a{color:var(--blue-text)}
.foot-nav a{position:absolute;top:21px;font-size:9.8px;color:#888}
.foot-nav a.active{color:var(--blue-text)}
</style>
</head>
<body>

<header>
  <div class="abs topbar">
    <nav class="main-nav">
      <a class="active" href="#" style="left:148px">Home</a>
      <a href="#" style="left:220px">About</a>
      <a href="#" style="left:294px">Services</a>
      <a href="#" style="left:378px">Portfolio</a>
      <a href="#" style="left:466px">News</a>
      <a href="#" style="left:544px">Contact</a>
    </nav>
    <div class="social">
      <span style="left:807px" aria-label="Social profile"></span>
      <span style="left:845px" aria-label="Social profile"></span>
      <span style="left:884px" aria-label="Social profile"></span>
    </div>
  </div>

  <div class="abs brand">
    <div class="brand-dot"></div>
    <div class="brand-name">Vexlo</div>
  </div>

  <div class="abs search">
    <span>Search our site...</span>
    <b>GO</b>
  </div>
</header>

<section>
  <div class="abs hero-photo" role="img" aria-label="Smiling team of colleagues in a bright office meeting"></div>
  <div class="abs hero-panel">
    <h1 class="hero-title">Providing Apps &amp;<br>Development</h1>
    <div class="hero-rule" style="top:121px"></div>
    <p class="hero-text">Lorem ipsum dolor sit amet, consectetur adipiscing elit. Praesent dolor nunc, rhon-cus porttitor bibendum in, placerat sed dui raesent suscipit consequat nunc, et</p>
    <div class="hero-rule" style="top:235px"></div>
    <a class="hero-btn" href="#">Get in touch</a>
  </div>
</section>

<section>
  <h2 class="abs h2" style="left:152px;top:517px">Lorem Ipsuming Eredtce salaing <em>teredirte ono lingstumb uni</em></h2>
  <p class="abs copy" style="left:152px;top:544px;width:494px">Vestibulum non consectetur urna. Ut non quam quam am congue rutrumon leo, vel vulputate Cras fermentum lectus vel erat adipiscing ullamcorper. Duis blandit mauris at purus mollis eu laoreet odio tempor. Maecenas viverra varius turpis, a aliquam mi dignissim id. In aliquam cursus consequat. Integer magna nulla, porttitor sed feugiat ac, ultricies sed neque. Donec ornare dui vel tortor ultricies lobortis. Nulla vel orci massa, fringilla posuere ipsum. Quisque eu lectus tortor, quis faucibus eros ono linyters gijod knoinsdf poleor.</p>
  <a class="abs more-link" href="#" style="left:152px;top:710px">FIND OUT MORE <i class="arrow"></i></a>

  <h2 class="abs h2" style="left:707px;top:517px">Lorem Ipsuming Eredtce</h2>
  <p class="abs copy" style="left:707px;top:544px;width:205px">Vestibulum non consectetur urna. Ut non quam quam am congue rutrumon leo, vel</p>
  <ul class="abs list" style="left:707px;top:0">
    <li style="top:605px">Pellentesque habitant morbi tris</li>
    <li style="top:639px">Malesuada fames ac turpis egesta</li>
    <li style="top:673px">Rhoncus elleno pertign salmseths</li>
  </ul>
  <a class="abs more-link dark" href="#" style="left:707px;top:710px">READ MORE <i class="arrow"></i></a>

  <div class="abs divider"></div>
</section>

<section>
  <article class="abs card" style="left:148px">
    <div class="card-img" role="img" aria-label="Colleagues reviewing charts beside a laptop" style="background:linear-gradient(135deg,#e8eef2,#b9cde0 60%,#7fa3c8)"></div>
    <span class="card-notch" style="border-top-color:#9db6cf"></span>
    <h3>Eredtce salaing</h3>
    <h4>CONSECTETUR</h4>
    <hr>
    <p>Lorem ipsum dolor sit amet, consectetur adipis ing elit. Praesent dolor nunc, rhoncus porttitorol bibendum in, placerat sed dui raesent suscipi.</p>
    <a class="more-link" href="#">MORE <i class="arrow"></i></a>
  </article>
  <article class="abs card" style="left:407px">
    <div class="card-img" role="img" aria-label="Man using a tablet among city towers" style="background:linear-gradient(135deg,#cfd8e0,#9aa9b6 55%,#6c7884)"></div>
    <span class="card-notch" style="border-top-color:#7d8995"></span>
    <h3>Eredtce salaing</h3>
    <h4>CONSECTETUR</h4>
    <hr>
    <p>Lorem ipsum dolor sit amet, consectetur adipis ing elit. Praesent dolor nunc, rhoncus porttitorol bibendum in, placerat sed dui raesent suscipi.</p>
    <a class="more-link" href="#">MORE <i class="arrow"></i></a>
  </article>
  <article class="abs card" style="left:665px">
    <div class="card-img" role="img" aria-label="Hand touching a ring of digital service icons" style="background:linear-gradient(135deg,#5f7f9c,#2f4a66 60%,#1e2f44)"></div>
    <span class="card-notch" style="border-top-color:#35506c"></span>
    <h3>Eredtce salaing</h3>
    <h4>CONSECTETUR</h4>
    <hr>
    <p>Lorem ipsum dolor sit amet, consectetur adipis ing elit. Praesent dolor nunc, rhoncus porttitorol bibendum in, placerat sed dui raesent suscipi.</p>
    <a class="more-link" href="#">MORE <i class="arrow"></i></a>
  </article>
</section>

<footer class="abs footer">
  <p class="copyright">Copyright 2013 <a href="#">Business Name</a> &nbsp;|&nbsp; All rights reserved</p>
  <nav class="foot-nav">
    <a class="active" href="#" style="left:636px">Home</a>
    <a href="#" style="left:682px">About</a>
    <a href="#" style="left:728px">Services</a>
    <a href="#" style="left:784px">Portfolio</a>
    <a href="#" style="left:842px">News</a>
    <a href="#" style="left:879px">Contact</a>
  </nav>
</footer>

</body>
</html>
```